PSD website for property company

Please read the brief thoroughly.

We are looking for a new website for a property group that does property acquisitions, property development and property management.
They buy, build and lease core inner city industrial assets in Sydney, Australia.
They also invest in residential developments.

Site menu
- Home page
- Property – sub menus include – Leasing ; Projects ; Investments ; Property Management
- Capital and finance
- About
- Contact

They like this website
https://www.verlo.com.au/

They want the site to be clean, modern and bold.
They like few colors, even black and white is OK to submit

They have a logo and style guide and useable images here:
http://www.kumet.net/temp/PelorisWeb2019.zip
The zip file is also attached to this project.
We have supplied some images to give you an idea, but we will also require you to provide at least 3 extra images from stock photos.
Use your imagination.

I am expecting a lot of similar designs, so be aware the photos you choose will be really important.
They want really 3 good stock photos used and supplied without charge.
Please not too generic, I repeat the quality of the photos is important.
You may provide several photos (but not in multiple submissions please) and we will choose the best three to be provided.

The winner will be selected on a single home page design and required to provide;
All photos use in original format without charge
A second ‘standard page’ template design based on the winning home page design

```html
<!DOCTYPE html>
<html lang="en">
<head>
<meta charset="utf-8">
<title>Peloris Property Group</title>
<link rel="stylesheet" href="https://fonts.googleapis.com/css2?family=Anton&family=Arimo:wght@400;700&family=Open+Sans:ital,wght@0,400;0,600;1,400&display=swap">
<style>
:root{
  --green:#566e36;
  --green-dark:#4a5f2e;
  --ink:#111;
  --text:#555;
  --dark:#2b2b2b;
  --footer:#333;
  --line:#e6e6e6;
  --white:#fff;
}
*{box-sizing:border-box;margin:0;padding:0}
html,body{width:1200px;height:4005px;overflow:hidden}
body{position:relative;background:var(--white);font-family:'Open Sans',sans-serif;color:var(--text)}
.abs{position:absolute}
.heading{font-family:'Arimo',sans-serif;font-weight:400;color:var(--ink);text-transform:uppercase;letter-spacing:-.5px}
.btn{position:absolute;background:var(--green);color:#fff;font-family:'Arimo',sans-serif;font-size:17px;text-transform:uppercase;display:flex;align-items:center;justify-content:center;border-radius:4px;letter-spacing:-.2px}
.divider{position:absolute;width:62px;height:14px}
.center{left:0;width:1200px;text-align:center}

/* header */
.logo{left:75px;top:22px;font-family:'Arimo',sans-serif;font-weight:700;font-size:34px;letter-spacing:9px;color:var(--ink)}
.nav{left:438px;top:32px;display:flex;gap:26px;font-size:15px;color:#444}
.nav .active{color:var(--green)}
.nav .active::before{content:"";display:inline-block;width:7px;height:7px;background:var(--green);transform:rotate(45deg);margin-right:8px;vertical-align:2px}
.search{left:936px;top:26px;width:187px;height:41px;border:1px solid #ccc;border-radius:4px;font-size:12px;color:#888;padding:12px 18px}
.search-btn{right:4px;top:5px;width:30px;height:29px;background:var(--green);border-radius:3px}

/* hero */
.hero-photo{left:0;top:108px;width:1200px;height:604px;background:linear-gradient(180deg,#f4f4f2 0%,#e9e6e0 45%,#8a7b68 70%,#6b6f5a 88%,#9a9a95 100%)}
.hero-title{left:831px;top:190px;font-family:'Anton',sans-serif;font-size:72px;line-height:79px;color:#111;text-transform:uppercase}
.hero-title span{color:var(--green)}
.dots{left:1168px;top:246px;display:flex;flex-direction:column;gap:10px}
.dots i{width:14px;height:14px;border:1.5px solid var(--green);border-radius:50%;display:block}
.dots i.on{background:var(--green)}

/* welcome */
.lead{font-style:italic;font-size:15px;line-height:27px;color:#555}
.body{font-size:15px;line-height:27px;color:#555}

/* acquisitions */
.acq{left:0;top:1218px;width:1200px;height:676px;background:var(--dark)}
.acq-green{left:626px;top:0;width:437px;height:676px;background:linear-gradient(115deg,var(--green) 0%,var(--green) 30%,#5d763b 30%,#5d763b 45%,var(--green) 45%,var(--green) 62%,#5d763b 62%,#5d763b 76%,var(--green) 76%)}
.count{left:121px;top:100px;font-family:'Anton',sans-serif;font-size:52px;color:#fff}
.count small{font-family:'Open Sans',sans-serif;font-size:16px;color:#888;margin-left:4px}
.acq .heading{color:#fff}
.acq-text{left:112px;top:362px;width:310px;font-size:15px;line-height:27px;color:#aaa}
.acq-photo{left:569px;top:106px;width:545px;height:362px;background:linear-gradient(180deg,#dfe7ee 0%,#cdd9e3 35%,#b79e83 55%,#6e7a5a 78%,#3f5330 100%)}
.acq-photo-next{left:1139px;top:106px;width:61px;height:362px;background:linear-gradient(180deg,#c9d1d7,#e5e7e8)}

/* projects */
.watermark{left:732px;top:2005px;font-family:'Arimo',sans-serif;font-weight:700;font-size:150px;color:#f3f3f3;white-space:nowrap;letter-spacing:4px}
.card{position:absolute;top:2123px;width:322px}
.card-photo{width:322px;height:357px}
.card-foot{height:61px;border-bottom:3px solid #eee;display:flex;justify-content:space-between;align-items:center;padding:0 3px}
.card-foot span{font-family:'Arimo',sans-serif;font-size:16px;color:#222;text-transform:uppercase}
.card-foot svg{width:24px;height:24px}

/* capital */
.person{left:676px;top:2595px;width:320px;height:474px;background:radial-gradient(ellipse at 50% 35%,#f0ece6 0%,#e8e4df 45%,#fff 75%)}

/* contact */
.contact{left:0;top:3071px;width:1200px;height:519px;background:linear-gradient(180deg,#2e3236 0%,#3a3e41 40%,#4a4a46 70%,#2c2b28 100%)}
.contact .heading{color:#fff}
.field{position:absolute;border:1px solid #6b6e70;border-radius:4px;font-size:14px;color:#aaa;padding:14px 18px}
.field.focus{border-color:#ddd;color:#fff}

/* footer */
.band{left:0;top:3590px;width:1200px;height:109px;background:var(--green);display:flex;align-items:center;justify-content:center;font-family:'Arimo',sans-serif;font-weight:700;font-size:34px;letter-spacing:9px;color:#fff}
.social{left:488px;top:3737px;display:flex;gap:8px}
.social div{width:50px;height:50px;display:flex;align-items:center;justify-content:center}
.contact-lines{font-size:14px;line-height:28px;color:#555}
.up-tab{left:575px;top:3904px;width:48px;height:38px;background:var(--footer)}
.bottom{left:0;top:3942px;width:1200px;height:63px;background:var(--footer);font-size:14px;color:#aaa;display:flex;align-items:center;justify-content:center}
.bottom b{color:var(--green);font-weight:400}
</style>
</head>
<body>

<header>
  <div class="abs logo">PELORIS</div>
  <nav class="abs nav">
    <span class="active">Home</span><span>Property</span><span>Capital and finance</span><span>About</span><span>Contact</span>
  </nav>
  <div class="abs search">Type Here...
    <span class="abs search-btn"><svg width="30" height="29" viewBox="0 0 30 29"><circle cx="14" cy="13" r="5" fill="none" stroke="#fff" stroke-width="2"/><line x1="17.5" y1="16.5" x2="21" y2="20" stroke="#fff" stroke-width="2"/></svg></span>
  </div>
</header>

<section>
  <div class="abs hero-photo" role="img" aria-label="Brick mid-rise building on a tree-lined city street"></div>
  <h1 class="abs hero-title">Peloris<br>Property<br><span>Group</span></h1>
  <div class="abs dots"><i></i><i></i><i></i><i class="on"></i><i></i><i></i></div>
</section>

<section>
  <h2 class="abs heading center" style="top:776px;font-size:42px">Welcome to Peloris</h2>
  <svg class="divider" style="left:569px;top:832px" viewBox="0 0 62 14"><line x1="0" y1="7" x2="62" y2="7" stroke="#566e36" stroke-width="2"/><rect x="26" y="2" width="10" height="10" transform="rotate(45 31 7)" fill="#566e36"/></svg>
  <p class="abs lead center" style="top:879px">Lorem Ipsum is simply dummy text of the printing and typesetting industry.<br>Lorem Ipsum has been the industry's standard dummy text ever since the 1500s,<br>when an unknown printer took a galley of</p>
  <p class="abs body center" style="top:977px">Lorem Ipsum is simply dummy text of the printing and typesetting industry. Lorem<br>Ipsum has been the industry's standard dummy text ever since the 1500s, when an<br>unknown printer took a galley of type and scrambled it to make a type specimen<br>book. It has survived not only five centuries</p>
  <div class="btn" style="left:511px;top:1105px;width:177px;height:51px">Learn More</div>
</section>

<section class="abs acq">
  <div class="abs acq-green"></div>
  <div class="abs count">01<small>/ 03</small></div>
  <h2 class="abs heading" style="left:112px;top:214px;font-size:42px;line-height:47px">Property<br>Acquisitions</h2>
  <svg class="divider" style="left:112px;top:324px" viewBox="0 0 62 14"><line x1="0" y1="7" x2="62" y2="7" stroke="#566e36" stroke-width="2"/><rect x="26" y="2" width="10" height="10" transform="rotate(45 31 7)" fill="#566e36"/></svg>
  <p class="abs acq-text">Lorem Ipsum is simply dummy text of the printing and typesetting industry. Lorem Ipsum has been the industry's standard dummy text ever since the.</p>
  <div class="btn" style="left:117px;top:505px;width:175px;height:50px">Learn More</div>
  <div class="abs acq-photo" role="img" aria-label="Row of colourful Victorian terrace houses under a cloudy sky"></div>
  <div class="abs acq-photo-next" role="img" aria-label="Next slide: modern apartment building"></div>
  <svg class="abs" style="left:772px;top:522px" width="136" height="66" viewBox="0 0 136 66">
    <rect x="12" y="13" width="40" height="40" transform="rotate(45 32 33)" fill="none" stroke="#fff" stroke-width="1.5"/>
    <rect x="84" y="13" width="40" height="40" transform="rotate(45 104 33)" fill="none" stroke="#fff" stroke-width="1.5"/>
    <path d="M22 33h20M22 33l6-6M22 33l6 6" stroke="#fff" stroke-width="1.5" fill="none"/>
    <path d="M94 33h20M114 33l-6-6M114 33l-6 6" stroke="#fff" stroke-width="1.5" fill="none"/>
  </svg>
</section>

<section>
  <div class="abs watermark" aria-hidden="true">PROJECTS</div>
  <h2 class="abs heading center" style="top:1953px;font-size:42px">Our Projects</h2>
  <svg class="divider" style="left:569px;top:2012px" viewBox="0 0 62 14"><line x1="0" y1="7" x2="62" y2="7" stroke="#566e36" stroke-width="2"/><rect x="26" y="2" width="10" height="10" transform="rotate(45 31 7)" fill="#566e36"/></svg>
  <p class="abs lead center" style="top:2043px">Lorem Ipsum is simply dummy text of the printing and typesetting industry.<br>Lorem Ipsum has been the industry's</p>

  <article class="card" style="left:78px">
    <div class="card-photo" role="img" aria-label="White country house with blue roof at dusk" style="background:linear-gradient(180deg,#b8b4aa 0%,#e5dfd4 40%,#c9c2b4 65%,#6a7a52 85%,#8e8f88 100%)"></div>
    <div class="card-foot"><span>Project Title</span><svg viewBox="0 0 24 24"><circle cx="12" cy="12" r="11" fill="#566e36"/><path d="M10 8l4 4-4 4" stroke="#fff" stroke-width="2" fill="none"/></svg></div>
  </article>
  <article class="card" style="left:438px">
    <div class="card-photo" role="img" aria-label="Grey two-storey family house with front garden" style="background:linear-gradient(180deg,#e8ecef 0%,#8f8c80 30%,#a9a79c 55%,#6f8a4a 80%,#5f7d3c 100%)"></div>
    <div class="card-foot"><span>Project Title</span><svg viewBox="0 0 24 24"><circle cx="12" cy="12" r="11" fill="#566e36"/><path d="M10 8l4 4-4 4" stroke="#fff" stroke-width="2" fill="none"/></svg></div>
  </article>
  <article class="card" style="left:800px">
    <div class="card-photo" role="img" aria-label="Glass facade of a modern building against a pale sky" style="background:linear-gradient(120deg,#d6dae4 0%,#c5cad6 45%,#6f8682 62%,#3e5752 78%,#a8b0b8 100%)"></div>
    <div class="card-foot"><span>Project Title</span><svg viewBox="0 0 24 24"><circle cx="12" cy="12" r="11" fill="#566e36"/><path d="M10 8l4 4-4 4" stroke="#fff" stroke-width="2" fill="none"/></svg></div>
  </article>
</section>

<section>
  <h2 class="abs heading" style="left:182px;top:2674px;font-size:42px">Capital &amp; Finance</h2>
  <svg class="divider" style="left:182px;top:2733px" viewBox="0 0 62 14"><line x1="0" y1="7" x2="62" y2="7" stroke="#566e36" stroke-width="2"/><rect x="26" y="2" width="10" height="10" transform="rotate(45 31 7)" fill="#566e36"/></svg>
  <p class="abs body" style="left:191px;top:2767px;width:410px">Lorem Ipsum is simply dummy text of the printing and typesetting industry. Lorem Ipsum has been the indu stry's standard dummy text ever since the 1500s, when an unknown printer took a galley of type and scrambled it to make a type specimen book.</p>
  <div class="btn" style="left:190px;top:2923px;width:175px;height:50px">Learn More</div>
  <div class="abs person" role="img" aria-label="Smiling woman in a white shirt holding a coin"></div>
</section>

<section class="abs contact" role="group" aria-label="Contact form over a lakeside house at dusk">
  <h2 class="abs heading center" style="top:58px;font-size:42px">Contact Us</h2>
  <svg class="divider" style="left:569px;top:115px" viewBox="0 0 62 14"><line x1="0" y1="7" x2="62" y2="7" stroke="#566e36" stroke-width="2"/><rect x="26" y="2" width="10" height="10" transform="rotate(45 31 7)" fill="#566e36"/></svg>
  <p class="abs center" style="top:146px;font-size:16px;color:#eee">If you need an have any Question for Contact Us ?</p>
  <div class="field focus" style="left:179px;top:213px;width:384px;height:51px">Name *</div>
  <div class="field" style="left:179px;top:275px;width:384px;height:51px">Email *</div>
  <div class="field" style="left:179px;top:337px;width:384px;height:51px">Phone *</div>
  <div class="field" style="left:573px;top:213px;width:446px;height:175px">Message *</div>
  <div class="btn" style="left:491px;top:407px;width:218px;height:50px">Send Us Message</div>
</section>

<footer>
  <div class="abs band">PELORIS</div>
  <div class="abs social">
    <div><svg width="50" height="50" viewBox="0 0 50 50"><rect x="11" y="11" width="28" height="28" transform="rotate(45 25 25)" fill="#fff" stroke="#566e36" stroke-width="2"/><circle cx="25" cy="25" r="5" fill="#566e36"/></svg></div>
    <div><svg width="50" height="50" viewBox="0 0 50 50"><rect x="11" y="11" width="28" height="28" transform="rotate(45 25 25)" fill="#eee"/><circle cx="25" cy="25" r="5" fill="#999"/></svg></div>
    <div><svg width="50" height="50" viewBox="0 0 50 50"><rect x="11" y="11" width="28" height="28" transform="rotate(45 25 25)" fill="#eee"/><circle cx="25" cy="25" r="5" fill="#999"/></svg></div>
    <div><svg width="50" height="50" viewBox="0 0 50 50"><rect x="11" y="11" width="28" height="28" transform="rotate(45 25 25)" fill="#eee"/><rect x="18" y="20" width="14" height="10" fill="none" stroke="#999" stroke-width="1.6"/><path d="M18 20l7 6 7-6" fill="none" stroke="#999" stroke-width="1.6"/></svg></div>
  </div>
  <p class="abs contact-lines center" style="top:3814px">info@peloris.com | Phone : 123 456 7890<br>Address : 101 Lorem ipsum simple text print industry</p>
  <div class="abs up-tab"><svg width="48" height="38" viewBox="0 0 48 38"><path d="M17 22l7-7 7 7M17 28l7-7 7 7" stroke="#566e36" stroke-width="2" fill="none"/></svg></div>
  <div class="abs bottom"><span>©<b>PELORIS</b> - 2019 All Rights Reserved. Privacy Policy &nbsp;| Tearms &amp; Conditions</span></div>
</footer>

</body>
</html>
```